Professional Letterhead for electronic use

I would like to inquire, if you could help me to create a letterhead, mostly for electronic use. Preferably in word file, with fixed letterhead design (header and footer), but will allow to add text on the main body of the letter. I usually operate online and would like to be able to add text, convert it to PDF and send as an attachment.
Target Market(s)
High net worth clients.
Industry/Entity Type
Real Estate Agent
Font styles to use
Other font styles liked:
- Century Gothic
Requirements
Must have
- Company name, logo, full address, email address, landline number, website address, Homestead Adjudicator logo, PELV logo, Company registration number
Nice to have
- Professional and elegant design

```html
<!DOCTYPE html>
<html lang="en">
<head>
<meta charset="utf-8">
<title>Velmora Estate Agents Letterhead</title>
<link href="https://fonts.googleapis.com/css2?family=Questrial&display=swap" rel="stylesheet">
<style>
  :root {
    --backdrop: #5c5c5c;
    --plum: #4a1a35;
    --orange: #e8562a;
    --orange-light: #f29152;
    --paper: #f8f7f5;
    --ink: #3a2030;
    --white: #ffffff;
  }
  * { box-sizing: border-box; margin: 0; padding: 0; }
  html, body { width: 1200px; height: 800px; overflow: hidden; }
  body {
    background: var(--backdrop);
    font-family: "Questrial", "Century Gothic", sans-serif;
    position: relative;
  }
  .letterhead {
    position: absolute;
    left: 330px; top: 18px;
    width: 540px; height: 764px;
    background: var(--paper);
    display: flex; flex-direction: column;
  }
  .header {
    position: relative;
    height: 118px;
    background: var(--plum);
    overflow: hidden;
  }
  .brand {
    position: absolute; left: 34px; top: 34px;
    display: flex; align-items: center; gap: 14px;
  }
  .brand-dot {
    width: 40px; height: 40px; border-radius: 50%;
    background: var(--orange);
  }
  .brand-name {
    color: var(--white);
    font-size: 24px; letter-spacing: 6px; line-height: 1;
  }
  .brand-tagline {
    color: var(--orange);
    font-size: 9px; letter-spacing: 4.5px; margin-top: 8px;
  }
  .header-decoration {
    position: absolute; right: 0; top: 0;
    width: 200px; height: 118px;
    background: linear-gradient(120deg, var(--orange-light) 0%, var(--orange) 45%, var(--plum) 100%);
  }
  .body-area { flex: 1; }
  .credentials {
    display: flex; align-items: flex-end; justify-content: space-between;
    padding: 0 30px 8px 34px;
  }
  .badges { display: flex; align-items: flex-end; gap: 12px; }
  .badge-ombudsman { width: 92px; height: 20px; background: #1f3f87; }
  .badge-pelv { width: 60px; height: 20px; border-radius: 50%; background: #2f8a3a; }
  .company-number { font-size: 8.5px; color: var(--ink); letter-spacing: 0.4px; }
  .footer {
    height: 30px;
    background: var(--plum);
    display: flex; align-items: center; justify-content: space-between;
    padding: 0 18px 0 34px;
    color: var(--white);
    font-size: 8.5px; letter-spacing: 0.3px;
  }
  .contact-item { display: flex; align-items: center; gap: 5px; white-space: nowrap; }
  .contact-icon { width: 8px; height: 8px; }
</style>
</head>
<body>
  <main class="letterhead">
    <header class="header">
      <div class="brand">
        <div class="brand-dot"></div>
        <div>
          <div class="brand-name">VELMORA</div>
          <div class="brand-tagline">ESTATE AGENTS</div>
        </div>
      </div>
      <div class="header-decoration" role="img" aria-label="Large flowing brand decoration in orange and plum"></div>
    </header>

    <section class="body-area"></section>

    <div class="credentials">
      <div class="badges">
        <div class="badge-ombudsman" role="img" aria-label="Homestead Adjudicator membership badge"></div>
        <div class="badge-pelv" role="img" aria-label="PELV membership badge"></div>
      </div>
      <div class="company-number">Company Number 07314582</div>
    </div>

    <footer class="footer">
      <span class="contact-item">
        <svg class="contact-icon" viewBox="0 0 10 10"><path d="M2 1l2 2-1 1.2c.6 1.2 1.6 2.2 2.8 2.8L7 6l2 2-1.4 1.4C4.6 9 1 5.4.6 2.4z" fill="var(--orange)"/></svg>
        02-071-448263
      </span>
      <span class="contact-item">
        <svg class="contact-icon" viewBox="0 0 10 10"><rect x="0.5" y="2" width="9" height="6" fill="none" stroke="var(--orange)"/><path d="M0.5 2l4.5 3.5L9.5 2" fill="none" stroke="var(--orange)"/></svg>
        info@velmora.co.uk
      </span>
      <span class="contact-item">
        <svg class="contact-icon" viewBox="0 0 10 10"><circle cx="5" cy="5" r="4.3" fill="none" stroke="var(--orange)"/><ellipse cx="5" cy="5" rx="2" ry="4.3" fill="none" stroke="var(--orange)"/><path d="M.7 5h8.6" stroke="var(--orange)"/></svg>
        www.velmora.co.uk
      </span>
      <span class="contact-item">
        <svg class="contact-icon" viewBox="0 0 10 10"><path d="M5 .5a3.3 3.3 0 0 1 3.3 3.3C8.3 6.3 5 9.5 5 9.5S1.7 6.3 1.7 3.8A3.3 3.3 0 0 1 5 .5z" fill="var(--orange)"/><circle cx="5" cy="3.8" r="1.2" fill="var(--plum)"/></svg>
        214A Larchmont Road, Kelsworth, London, NW9 4QT
      </span>
    </footer>
  </main>
</body>
</html>
```